Design Product Packaging For Face Mask Brand

We need packaging designed for a new product, "Harbor Bloom Cover" a made in canada multi layer poly cotton reusable non-medical face mask for all people. The mask ties in the back behind the head.

Preference is a 4x6' flat polybag or 5x7" resealable stand up bag.

We would like to see bold easy to read colour block designs that use the colour pink. The final design should communicate a simple, high fashion, bold fun quality product.

IMG-9732 and 9733 are of the actual product.
Img_9695 and 9786 are our logos.
Vintageladyshoppinggreenmask is an image on our website.
2020-04_VK is the style of image we would like to have on the front of the packaging.
Maskonworldoff is an example of fun cute wording.

Please leave space for upc on the back of the package aswell. Open to your creativity in terms of design but colors must stay the same as brand.

Thank you all for you time and submissions.

Harbor Bloom Cover xoxo

Target Market(s)

Canada/USA civilians, non-health workers

Industry/Entity Type

Fashion

Font styles to use
Sans Serif

Colors
ffffff
feeeee
f9d9e8
eea4c8
e667a6
e34298
86cfc6
33b8a4
87cfc6

Requirements
Must have
• our logo, brand colors, upc on back
Nice to have
• Bold Font
Should not have
• Hard to read handwriting

```html
<!DOCTYPE html>
<html lang="en">
<head>
<meta charset="utf-8">
<title>Harbor Bloom Cover – Pouch Front and Back</title>
<link href="https://fonts.googleapis.com/css2?family=Bodoni+Moda:wght@700&family=Caveat+Brush&family=Poppins:wght@300;500;600&family=Oswald:wght@600&display=swap" rel="stylesheet">
<style>
  :root{
    --bg:#d9c5c4;
    --pink:#e0197f;
    --pink-deep:#c8166f;
    --pink-seal:#d91a7c;
    --pink-soft:#e667a6;
    --blush:#f9d9e8;
    --white:#ffffff;
    --silver:#e6e3e4;
    --coral:#ee6a6a;
    --teal:#33b8a4;
  }
  *{box-sizing:border-box;margin:0;padding:0}
  html,body{width:1200px;height:896px;overflow:hidden;background:var(--bg)}
  .canvas{position:relative;width:1200px;height:896px}

  .pouch{position:absolute;top:128px;width:405px;height:636px;background:var(--pink-seal);overflow:hidden}
  .pouch--front{left:119px}
  .pouch--back{left:663px}
  .pouch__body{position:absolute;inset:33px 33px 0 33px;background:linear-gradient(180deg,var(--pink) 0%,var(--pink-deep) 40%,var(--pink) 100%)}

  .brand-tag{position:absolute;display:flex;align-items:center;gap:4px;font-family:'Oswald',sans-serif;font-weight:600;color:var(--blush);text-transform:uppercase;line-height:1}
  .brand-tag__dot{width:9px;height:9px;border-radius:50%;background:var(--coral)}
  .pouch--front .brand-tag{top:40px;left:0;right:0;justify-content:center;font-size:12px}
  .pouch--back .brand-tag{top:40px;right:38px;font-size:9px}

  .front-title{position:absolute;top:150px;left:0;right:0;text-align:center;font-family:'Caveat Brush',cursive;font-weight:400;color:var(--silver);font-size:92px;line-height:102px;transform:rotate(-4deg)}
  .front-foot{position:absolute;left:0;right:0;bottom:0;height:135px}
  .front-foot svg{position:absolute;inset:0;width:100%;height:100%}
  .front-foot__name{position:absolute;left:0;right:0;bottom:32px;text-align:center;font-family:'Oswald',sans-serif;font-weight:600;font-size:17px;color:var(--coral);display:flex;justify-content:center;align-items:center;gap:6px}
  .front-foot__square{width:10px;height:10px;background:var(--teal)}

  .back-title{position:absolute;top:24px;left:33px;font-family:'Bodoni Moda',serif;font-weight:700;font-size:30px;line-height:36.5px;color:var(--blush)}

  .details{position:absolute;top:222px;left:0;right:0;height:160px;background:var(--silver);padding:9px 0 0 34px;font-family:'Poppins',sans-serif;font-weight:500;font-size:7.6px;color:var(--pink)}
  .details__heading{font-size:9.5px;font-weight:600;line-height:12px;margin-bottom:3px}
  .details__list li{list-style:none;line-height:17px;white-space:nowrap}
  .details__list li::before{content:"• "}
  .details__list--grid{display:grid;grid-template-columns:130px 1fr}

  .disclaimer{position:absolute;top:398px;left:34px;width:336px;font-family:'Poppins',sans-serif;font-weight:300;font-size:6.6px;line-height:11.1px;color:var(--blush)}

  .back-wave{position:absolute;left:0;right:0;bottom:0;width:100%;height:136px}

  .back-brand{position:absolute;top:548px;left:34px;width:205px;color:var(--blush)}
  .back-brand__name{font-family:'Oswald',sans-serif;font-size:19px;font-weight:600;line-height:22px;letter-spacing:.3px}
  .back-brand__origin{font-family:'Poppins',sans-serif;font-weight:500;font-size:6.8px;line-height:10px;margin-top:3px}
  .contact{display:flex;gap:14px;margin-top:9px;font-family:'Poppins',sans-serif;font-weight:300;font-size:6.8px;line-height:10px;align-items:center;white-space:nowrap}
  .contact__item{display:flex;align-items:center;gap:3px}

  .upc-space{position:absolute;top:546px;left:246px;width:139px;height:68px;background:var(--white);border-radius:9px}
</style>
</head>
<body>
<main class="canvas">
  <section class="pouch pouch--front" aria-label="Pouch front">
    <div class="pouch__body"></div>
    <div class="brand-tag"><i class="brand-tag__dot"></i>Harbor Bloom Cover</div>
    <h1 class="front-title">Harbor<br>Bloom<br>Cover</h1>
    <div class="front-foot">
      <svg viewBox="0 0 405 135" preserveAspectRatio="none" aria-hidden="true">
        <path d="M0 66 C80 35 150 0 210 0 C280 2 340 40 405 58 L405 135 L0 135Z" fill="var(--silver)"/>
      </svg>
      <div class="front-foot__name"><span class="front-foot__square"></span>HARBOR BLOOM COVER</div>
    </div>
  </section>

  <section class="pouch pouch--back" aria-label="Pouch back">
    <div class="pouch__body"></div>
    <div class="brand-tag"><i class="brand-tag__dot"></i>Harbor Bloom Cover</div>
    <h2 class="back-title">Classic<br>Reusable<br>Multi Layer<br>Face Mask<br>With Pocket</h2>

    <div class="details">
      <h3 class="details__heading">DETAILS</h3>
      <ul class="details__list">
        <li>Fabrics may vary: 100% Poly Cotton, Cotton Blends (98% Cotton, 2% Elastane)</li>
        <li>Machine wash warm, only Non-Chlorine bleach when needed</li>
      </ul>
      <ul class="details__list details__list--grid">
        <li>Material and color may vary</li><li>Non-medical grade</li>
        <li>Not intended for clinical use</li><li>Cotton thread</li>
        <li>Reusable</li><li>Tie straps</li>
        <li>To be laundered before use</li><li>Tumble dry low</li>
        <li>Machine Washable</li><li>Machine wash in longest highest temperature</li>
        <li>Please wash before use</li><li>Mask has pocket for filter</li>
      </ul>
    </div>

    <p class="disclaimer">*It has been suggested that shop towel, dried unscented baby wipes and coffee filters can be used as filters.<br>While the purpose is to protect, please understand that this mask is not a replacement for medical grade Personal Protective Equipment, and is not intended to replace other recommended measures to stop the community spread of COVID-19. Please continue to practice social distancing, washing your hands and refraining from touching your face. We recommend you consult a health care professional should you be in a circumstance that requires medical grade Personal Protective Equipment.</p>

    <svg class="back-wave" viewBox="0 0 405 136" preserveAspectRatio="none" aria-hidden="true">
      <path d="M0 40 C90 0 200 18 270 34 C330 48 380 30 405 18 L405 136 L0 136Z" fill="var(--pink-soft)" opacity=".45"/>
    </svg>

    <div class="back-brand">
      <h3 class="back-brand__name">HARBOR BLOOM COVER</h3>
      <p class="back-brand__origin">Designed and manufactured in Toronto, Canada</p>
      <div class="contact">
        <span class="contact__item"><svg width="7" height="7" viewBox="0 0 10 10"><path d="M2 1l2 2-1 1.5a6 6 0 0 0 2.5 2.5L7 6l2 2-1.5 1.5C4 9 1 6 .5 2.5Z" fill="currentColor"/></svg>1-555-014-2290</span>
        <span class="contact__item"><svg width="7" height="6" viewBox="0 0 10 8"><rect width="10" height="8" rx="1" fill="currentColor"/></svg>hello@harborbloomcover.com</span>
      </div>
    </div>

    <div class="upc-space" role="img" aria-label="Space reserved for UPC barcode"></div>
  </section>
</main>
</body>
</html>
```